Business card design needed - Halvey Group

Halvey Group are qualified, licensed builders who provide quality, value for money solutions for anyone looking to renovate, add or extend as well as those looking to build a new home.

Read more: http://www.renovista-listings.com.au/connect/halvey/service/582031#ixzz7kWpR4m2q

Hi All, Website will NOT let me load any files so please email me for our logo.

Cheers

Industry/Entity Type

Business

Contact Information for Business Card

Halvey Group Pty. Ltd.
Marcus Halvey
0412 587 264
ACT Licensed Builders #2094371
ABN 52 781 406 239
Marcus@halvey-build.com.au

Requirements
Must have
• Name
Mobile
Email
Builders License #
ABN
Company Logo as card background (See Attached)
Matched Black reverse side of card
Should not have
• Any other images or graphic aside from logo background

```html
<!DOCTYPE html>
<html lang="en">
<head>
<meta charset="utf-8">
<title>Halvey Group – Business Card</title>
<link href="https://fonts.googleapis.com/css2?family=Cabin:wght@400;700&display=swap" rel="stylesheet">
<style>
  :root {
    --backdrop: #2b2b2d;
    --card-white: #ffffff;
    --card-white-shade: #e9eaec;
    --card-navy: #0d1424;
    --brand-blue: #2c3a9c;
    --ink: #141414;
    --muted-grey: #8c8f94;
    --skyline-grey: #d3d5d8;
    --rule-grey: #b9bcc1;
  }
  * { box-sizing: border-box; margin: 0; padding: 0; }
  html, body {
    width: 1200px; height: 900px; overflow: hidden;
    background: var(--backdrop);
    font-family: "Cabin", "Gill Sans", sans-serif;
  }
  .sheet {
    position: relative; width: 1200px; height: 900px;
    display: flex; flex-direction: column; align-items: center;
    justify-content: center; gap: 42px;
  }
  .card {
    position: relative; width: 620px; height: 379px; overflow: hidden;
    box-shadow: 0 10px 30px rgba(0,0,0,.45);
  }

  /* Front */
  .card--front {
    background: linear-gradient(160deg, var(--card-white) 35%, var(--card-white-shade) 100%);
  }
  .skyline-backdrop {
    position: absolute; right: 0; bottom: 0; width: 470px; height: 250px;
    background: linear-gradient(180deg, rgba(211,213,216,0) 0%, var(--skyline-grey) 55%, var(--skyline-grey) 100%);
    opacity: .75;
    clip-path: polygon(0 100%, 0 78%, 40% 60%, 70% 15%, 100% 30%, 100% 100%);
  }
  .front-mark {
    position: absolute; top: 42px; right: 40px;
    display: flex; align-items: center; gap: 10px;
  }
  .front-mark__square { width: 18px; height: 18px; background: var(--brand-blue); }
  .front-mark__name {
    font-weight: 700; font-size: 24px; letter-spacing: 1px;
    text-transform: uppercase; color: var(--muted-grey);
  }
  .contact {
    position: absolute; left: 44px; top: 140px; color: var(--ink);
  }
  .contact__name { color: var(--brand-blue); font-size: 24px; font-weight: 400; line-height: 1.1; }
  .contact__role { font-size: 18px; font-weight: 700; margin-top: 2px; }
  .contact__company { font-size: 18px; font-weight: 700; margin-top: 26px; }
  .contact__line { font-size: 18px; line-height: 1.3; }
  .contact__label { color: var(--brand-blue); display: inline-block; width: 16px; }
  .contact__legal { font-size: 12px; color: #333; margin-top: 20px; line-height: 1.3; }

  /* Back */
  .card--back { background: var(--card-navy); }
  .back-mark {
    position: absolute; inset: 0;
    display: flex; align-items: center; justify-content: center; gap: 18px;
  }
  .back-mark__square { width: 34px; height: 34px; background: var(--brand-blue); }
  .back-mark__name {
    font-weight: 700; font-size: 50px; letter-spacing: 2px;
    text-transform: uppercase; color: var(--card-white);
  }
  .back-rule {
    position: absolute; left: 90px; right: 90px; top: 232px;
    height: 2px; background: var(--rule-grey); opacity: .6;
  }
</style>
</head>
<body>
<main class="sheet">
  <section class="card card--front" aria-label="Business card front">
    <div class="skyline-backdrop" role="img" aria-label="Faint city skyline decoration"></div>
    <div class="front-mark">
      <span class="front-mark__square"></span>
      <span class="front-mark__name">Halvey Group</span>
    </div>
    <div class="contact">
      <p class="contact__name">Marcus Halvey</p>
      <p class="contact__role">Founder and owner</p>
      <p class="contact__company">Halvey Group Pty. Ltd.</p>
      <p class="contact__line"><span class="contact__label">p</span>0412 587 264</p>
      <p class="contact__line"><span class="contact__label">e</span>Marcus@halvey-build.com.au</p>
      <p class="contact__legal">ACT Licensed Builders #2094371<br>ABN 52 781 406 239</p>
    </div>
  </section>

  <section class="card card--back" aria-label="Business card back">
    <div class="back-mark">
      <span class="back-mark__square"></span>
      <span class="back-mark__name">Halvey Group</span>
    </div>
    <div class="back-rule"></div>
  </section>
</main>
</body>
</html>
```